Tovrelan Ltda

Logo design focused on: - Construction of civil works - Electrical services - Metal structures - Equipment rental Tomás Ibarra Leiva Manager tovrelan.ltda@brevomail.example 56 9 48215037 Quelitoco s / n, Sorimar, San Pedro de Atacama

Building

Colors
33a6d7
0292cd
33b8a4
0555a3

```html
<!DOCTYPE html>
<html lang="es">
<head>
<meta charset="utf-8">
<title>Tovrelan Ltda – Tarjeta de presentación</title>
<link href="https://fonts.googleapis.com/css2?family=Work+Sans:wght@400;500;600&display=swap" rel="stylesheet">
<style>
  :root {
    --bg: #2a2a2b;
    --card-dark: #1c1d1f;
    --paper: #ffffff;
    --sky: #33a6d7;
    --azure: #0292cd;
    --teal: #33b8a4;
    --navy: #0555a3;
    --ink: #444548;
  }
  * { margin: 0; padding: 0; box-sizing: border-box; }
  html, body { width: 1200px; height: 930px; overflow: hidden; }
  body {
    background: var(--bg);
    font-family: "Work Sans", Arial, sans-serif;
    position: relative;
  }
  .card {
    position: absolute;
    width: 600px;
    height: 340px;
    overflow: hidden;
    box-shadow: 0 14px 30px rgba(0,0,0,.45);
  }
  /* Front */
  .card-front {
    left: 90px; top: 90px;
    background: var(--card-dark);
    display: flex; align-items: center; justify-content: center;
  }
  .brand { display: flex; align-items: center; gap: 18px; }
  .brand-dot {
    width: 64px; height: 64px; border-radius: 50%;
    background: var(--azure);
  }
  .brand-name {
    font-size: 44px; font-weight: 500; letter-spacing: 2px;
    color: var(--sky); text-transform: uppercase;
  }
  /* Back */
  .card-back { left: 510px; top: 500px; background: var(--paper); }
  .back-art { position: absolute; inset: 0; }
  .tab {
    position: absolute; left: -10px; top: 76px;
    width: 22px; height: 48px; border-radius: 6px;
    background: var(--navy);
  }
  .person { position: absolute; left: 34px; top: 72px; }
  .person-name {
    font-size: 25px; font-weight: 600; color: var(--navy);
    text-transform: uppercase; letter-spacing: .3px;
  }
  .person-role { font-size: 17px; color: var(--teal); margin-top: 2px; }
  .contact { position: absolute; left: 44px; top: 140px; list-style: none; }
  .contact li {
    display: flex; align-items: center; gap: 14px;
    font-size: 16px; color: var(--ink); margin-bottom: 6px;
  }
  .contact svg { width: 16px; height: 16px; flex: none; }
  .address {
    position: absolute; right: 36px; top: 30px;
    font-size: 14px; color: var(--ink); line-height: 1.45; text-align: left;
  }
  .services {
    position: absolute; right: 18px; top: 240px; list-style: none; text-align: right;
  }
  .services li {
    font-size: 13.5px; color: var(--teal); line-height: 1.55;
    display: flex; align-items: center; justify-content: flex-end; gap: 12px;
  }
  .services li::after {
    content: ""; width: 6px; height: 6px; background: var(--azure);
  }
</style>
</head>
<body>

  <section class="card card-front" aria-label="Anverso de la tarjeta">
    <div class="brand">
      <span class="brand-dot"></span>
      <span class="brand-name">Tovrelan Ltda</span>
    </div>
  </section>

  <section class="card card-back" aria-label="Reverso de la tarjeta">
    <svg class="back-art" viewBox="0 0 600 340" preserveAspectRatio="none" aria-hidden="true">
      <defs>
        <linearGradient id="darkFill" x1="0" y1="1" x2="1" y2="0">
          <stop offset="0" stop-color="#4a4b4d"/>
          <stop offset="1" stop-color="#1c1d1f"/>
        </linearGradient>
      </defs>
      <path d="M600,120 C430,120 330,170 300,340 L600,340 Z" fill="var(--teal)"/>
      <path d="M600,124 C434,124 334,174 304,340 L600,340 Z" fill="var(--sky)"/>
      <path d="M600,128 C438,128 338,178 308,340 L600,340 Z" fill="var(--azure)"/>
      <path d="M600,132 C442,132 342,182 312,340 L600,340 Z" fill="var(--navy)"/>
      <path d="M600,136 C446,136 346,186 316,340 L600,340 Z" fill="url(#darkFill)"/>
    </svg>

    <span class="tab"></span>

    <div class="person">
      <h1 class="person-name">Tomás Ibarra Leiva</h1>
      <p class="person-role">Gerente</p>
    </div>

    <ul class="contact">
      <li>
        <svg viewBox="0 0 16 16"><path d="M4 1.5 6 5 4.6 6.4c.9 1.9 2.3 3.3 4.2 4.2L10.2 9l3.5 2-1 2.6c-.3.6-1 .9-1.6.7C6.5 13 3 9.5 1.7 4.9c-.2-.6.1-1.3.7-1.6z" fill="var(--azure)"/></svg>
        +56 9 48215037
      </li>
      <li>
        <svg viewBox="0 0 16 16"><rect x="1.5" y="3.5" width="13" height="9" fill="none" stroke="var(--navy)" stroke-width="1.4"/><path d="M1.5 3.5 8 9l6.5-5.5" fill="none" stroke="var(--navy)" stroke-width="1.4"/></svg>
        tovrelan.ltda@brevomail.example
      </li>
    </ul>

    <p class="address">Quelitoco s/n, Sorimar,<br>San Pedro de Atacama</p>

    <ul class="services">
      <li>Construcción de Obras Civiles</li>
      <li>Servicios eléctricos</li>
      <li>Estructuras metálicas</li>
      <li>Arriendo de Equipos</li>
    </ul>
  </section>

</body>
</html>
```